Brochure design for 3D ultrasound company

I am looking for a clean and modern and edgy brochure for my ultrasound company. We are a fairly new company specialize in 3D/4D ultrasounds.Our brochures will be placed in OB-GYN offices in high end areas around Los Angeles, so we need something that will stand out and capture a modern woman's attention. Our logo is currently in the process of being designed, so I don't have a picture to provide quite yet, however it will be our company name"Kite + Fern" written in a special font that looks like neon lights. I will attach a few images of what our logo will be like, and some initial content that can help provide the layout we would like for the brochure. please feel free to also take a look at our website. www.kitefernscans.example.

Target Market(s)

Upscale trendy women.

Colors
eea4c8
33a6d7
fee18a

Requirements
Should not have
• too many colors.

```html
<!DOCTYPE html>
<html lang="en">
<head>
<meta charset="utf-8">
<title>Kite + Fern – Services + Pricing</title>
<link rel="stylesheet" href="https://fonts.googleapis.com/css2?family=Oswald:wght@400;500&family=Montserrat:wght@300;400&display=swap">
<style>
:root{
  --ink:#2b2b2b;
  --brown:#4e4237;
  --muted:#8a8a8a;
  --coral:#f07a7a;
  --sky:#d3f6fb;
  --sky-deep:#b4e8f3;
  --blush:#fccaca;
  --rule:#b9b9b9;
  --gold-rule:#e5d6a8;
}
*{margin:0;padding:0;box-sizing:border-box}
html,body{width:1200px;height:783px;overflow:hidden;background:#fff}
body{font-family:"Montserrat",sans-serif;color:var(--ink);position:relative}
.canvas{position:relative;width:1200px;height:783px;overflow:hidden}
.abs{position:absolute}

/* left column */
.hero-photo{left:0;top:0;width:402px;height:640px;
  background:
    linear-gradient(to bottom,rgba(255,255,255,0) 55%,#fff 100%),
    radial-gradient(ellipse at 45% 30%,#f5d8d4 0%,#e9a9b4 30%,rgba(233,169,180,0) 60%),
    linear-gradient(135deg,#4b5a4a 0%,#c98a9c 45%,#f1c9d1 70%,#fff 100%);}
.popular-title{left:24px;top:247px;font-family:"Oswald",sans-serif;font-weight:500;font-size:29px;color:var(--brown);letter-spacing:.2px;white-space:nowrap}
.feature-box{left:25px;top:293px;width:354px;height:255px;border:1px dashed var(--rule)}
.feature-name{left:36px;top:306px;font-size:21px;font-weight:400;color:var(--ink)}
.feature-list{left:35px;top:338px;list-style:none;font-size:16px;line-height:26.3px}
.feature-list li::before{content:"· ";}
.price{border-radius:50%;display:flex;align-items:center;justify-content:center;font-family:"Montserrat",sans-serif;color:var(--ink);box-shadow:2px 5px 6px rgba(0,0,0,.18)}
.price-feature{left:277px;top:448px;width:113px;height:113px;background:var(--sky-deep);font-size:23px}
.cta{left:0;width:402px;text-align:center;color:var(--muted);font-size:18.5px;line-height:26px;font-weight:300}

/* right column */
.backdrop{left:402px;top:0;width:798px;height:783px}
.page-title{left:402px;width:746px;top:28px;text-align:center;font-family:"Oswald",sans-serif;font-weight:500;font-size:50px;color:var(--brown);letter-spacing:.5px}
.services-frame{left:438px;top:99px;width:707px;height:644px;border:1px dashed var(--rule)}
.intro{left:440px;top:122px;width:703px;text-align:center;font-size:19px;line-height:27px;color:#6f6f6f;font-weight:300}
.menu{left:439px;top:197px;width:705px;height:545px;background:rgba(255,255,255,.92);border-top:1px dashed var(--rule)}
.tier-name{left:457px;font-size:19px;color:var(--coral);font-weight:400}
.tier-list{left:487px;font-size:15.3px;line-height:26.8px;padding-left:0}
.tier-list li{list-style:disc}
.tier-photo{left:853px;width:195px;border-radius:14px}
.price-tier{width:90px;height:90px;background:var(--sky);font-size:19px}
.divider{left:448px;width:686px;border-top:1px dashed var(--gold-rule)}
</style>
</head>
<body>
<main class="canvas">

  <!-- left column -->
  <div class="abs hero-photo" role="img" aria-label="Photo of an expectant mother in a white dress covering her eyes amid pink smoke"></div>
  <h2 class="abs popular-title">OUR MOST POPULAR PACKAGE</h2>
  <div class="abs feature-box"></div>
  <h3 class="abs feature-name">THE BIG REVEAL</h3>
  <ul class="abs feature-list">
    <li>25 minute 3D/4D/HD live session</li>
    <li>5 black and white pictures</li>
    <li>5 color pictures</li>
    <li>Email or USB flash drive with all images</li>
    <li>Record and hear heartbeat</li>
    <li>Confirm gender</li>
  </ul>
  <div class="abs price price-feature">$225.00</div>

  <p class="abs cta" style="top:568px">Ready for your baby’s first<br>photoshoot?</p>
  <p class="abs cta" style="top:632px">Give us a call to schedule an<br>appointment (555) 014-2290</p>
  <p class="abs cta" style="top:696px">or visit our website<br>www.kitefernscans.example</p>

  <!-- right column -->
  <svg class="abs backdrop" viewBox="0 0 798 783" aria-hidden="true">
    <polygon points="0,8 210,200 80,783 0,783" fill="var(--sky)"/>
    <polygon points="478,0 798,391 798,0" fill="var(--blush)"/>
    <polygon points="86,783 390,535 160,783" fill="var(--blush)" opacity=".8"/>
  </svg>

  <h1 class="abs page-title">SERVICES + PRICING</h1>
  <div class="abs services-frame"></div>
  <p class="abs intro">We are available for private in-home screenings, gender reveals,<br>baby showers, or any other special occasion!</p>

  <section class="abs menu"></section>

  <h3 class="abs tier-name" style="top:213px">PEEK-A-BOO:</h3>
  <ul class="abs tier-list" style="top:237px">
    <li>15 minute 2D session</li>
    <li>3 black and white images</li>
    <li>listen to baby’s heartbeat</li>
    <li>Confirm gender</li>
  </ul>
  <div class="abs tier-photo" style="top:210px;height:143px;background:linear-gradient(135deg,#d9d2cb,#c4977f 60%,#e4d9d2)" role="img" aria-label="Photo of hands holding an ultrasound print against a pregnant belly"></div>
  <div class="abs price price-tier" style="left:1020px;top:272px">$125.00</div>

  <div class="abs divider" style="top:367px"></div>

  <h3 class="abs tier-name" style="top:373px">HELLO, MOMMA:</h3>
  <ul class="abs tier-list" style="top:397px">
    <li>15 minute 3D/4D /HD live session</li>
    <li>3 black and white images</li>
    <li>2 color images</li>
    <li>Listen to baby’s heartbeat</li>
    <li>Confirm gender</li>
  </ul>
  <div class="abs tier-photo" style="top:402px;height:121px;background:linear-gradient(135deg,#f6ece9,#e9bfae 55%,#f3e3de)" role="img" aria-label="Photo of a plush teddy bear resting on a pregnant belly"></div>
  <div class="abs price price-tier" style="left:1024px;top:442px">$165.00</div>

  <div class="abs divider" style="top:548px"></div>

  <h3 class="abs tier-name" style="top:561px">V.I.B (VERY IMPORTANT BABY):</h3>
  <ul class="abs tier-list" style="top:585px;left:489px">
    <li>30 min 3D/4D/HD live session on our projector</li>
    <li>10 color images</li>
    <li>Email or USB with all images</li>
    <li>Record and hear heartbeat</li>
    <li>Confirm gender</li>
  </ul>
  <div class="abs tier-photo" style="top:563px;height:143px;background:linear-gradient(135deg,#c99a7d,#e6d6cf 45%,#5d7694 80%)" role="img" aria-label="Photo of a couple holding boy and girl tags over a pregnant belly"></div>
  <div class="abs price price-tier" style="left:1027px;top:622px">$325.00</div>

</main>
</body>
</html>
```